Design 2 8x10 one page sales brochures for KELMORA, a cloud service provider.

We’re open to fun and creative, yet must be clean, bold and professional.

***The winning designer will also be hired to design a handful of other brochures for us after the contest***

We understand the value of feedback and will work closely with every design to create the perfect sales brochure!

Should be printer friendly, primarily white so doesn’t consume a lot of printer ink
Colors - grey, black, light blue, llight green
We are a fun, easy to work with technology company and the brochures need to reflect taht.

Don't hesitate to ask any questions, thanks!

We need two designs, each one page 8x10"
#1 Why we're Kel
#2 KELTalk

Target Market(s)

Small and medium sized business owners

Industry/Entity Type

Telecommunications

Font styles to use
Sans Serif

Requirements
Must have
• Clean, professional designs. We're a fun tech company.
• Visually appealing
Nice to have
• graphs, charts, diagrams, etc
Should not have
• not sure.

```html
<!DOCTYPE html>
<html lang="en">
<head>
<meta charset="utf-8">
<title>KELMORA sales brochures</title>
<link rel="stylesheet" href="https://fonts.googleapis.com/css2?family=Source+Sans+3:wght@400;600;700&display=swap">
<style>
:root{
  --blue:#29a9e1;
  --blue-soft:rgba(41,169,225,.78);
  --charcoal:#58595b;
  --ink:#4d4d4f;
  --grey-text:#6d6e71;
  --stage:#dcdddf;
  --white:#ffffff;
  --photo-a:#c9ccc9;
  --photo-b:#8e969c;
}
*{box-sizing:border-box;margin:0;padding:0}
html,body{width:1200px;height:773px;overflow:hidden}
body{background:var(--stage);font-family:"Source Sans 3",sans-serif;color:var(--grey-text);position:relative}
.brochure{position:absolute;top:57px;width:529px;height:660px;background:var(--white);box-shadow:5px 6px 10px rgba(0,0,0,.28);overflow:hidden}
.brochure--why{left:58px}
.brochure--talk{left:628px}
.masthead{position:absolute;left:0;top:0;width:100%;height:51px;background:var(--charcoal);border-bottom:3px solid var(--white)}
.wordmark{position:absolute;left:20px;top:10px;font-size:26px;font-weight:700;color:var(--white);letter-spacing:.5px}
.masthead__tag{position:absolute;right:18px;top:20px;font-size:13px;color:var(--white)}
.masthead__tag--bold{font-weight:700;font-size:12px;top:21px;right:14px}
.hero{position:absolute;left:0;top:55px;width:100%;background:linear-gradient(115deg,var(--photo-a),var(--photo-b) 55%,#d8dcd8)}
.brochure--why .hero{height:268px}
.brochure--talk .hero{height:236px;background:linear-gradient(105deg,#e4e7ea,#b9c3cc 60%,#9aa6ae)}
.hero__headline{position:absolute;left:20px;top:100px;font-size:19.5px;line-height:25px;color:var(--white);font-weight:400;letter-spacing:.3px}
.hero-band{position:absolute;left:0;width:100%;background:var(--blue-soft);color:var(--white)}
.brochure--why .hero-band{top:245px;height:78px;padding:13px 15px 0 21px}
.hero-band__title{font-size:11px;font-weight:700}
.hero-band__text{font-size:10.6px;line-height:12.6px;text-align:justify}
.brochure--talk .hero-band{top:245px;height:46px;padding-top:8px;text-align:center;font-size:12.5px;font-weight:700;line-height:16px}
.col{position:absolute;font-size:10.3px;line-height:12.3px;text-align:justify}
.col p+p{margin-top:11px}
.col--left{left:20px;top:339px;width:230px}
.col--right{left:285px;top:339px;width:225px}
.col__head{font-size:11px;color:var(--ink);margin-bottom:5px;text-align:left}
.col__lead{font-size:11px;color:var(--ink);text-align:left;line-height:13px;margin-top:12px}
.tab{position:absolute;left:0;width:245px;height:28px;color:var(--white);font-size:11.5px;font-weight:700;padding:6px 0 0 20px}
.tab svg{position:absolute;left:0;top:0;z-index:0}
.tab span{position:relative}
.brochure--why .tab{top:469px}
.brochure--talk .tab{top:467px}
.checklist{position:absolute;left:20px;list-style:none;font-size:13.2px;color:var(--grey-text)}
.checklist li{height:22.5px;display:flex;align-items:center;gap:9px}
.brochure--why .checklist{top:503px}
.brochure--talk .checklist{top:501px}
.services{position:absolute;left:282px;top:521px;display:flex;gap:11px}
.service{width:50px;text-align:center}
.service__badge{width:50px;height:50px;border-radius:50%;background:var(--white);border:2px solid #eeeeef;box-shadow:0 2px 3px rgba(0,0,0,.15);display:flex;align-items:center;justify-content:center}
.service__name{font-size:8px;color:var(--grey-text);margin-top:10px;white-space:nowrap;margin-left:-8px;margin-right:-8px}
.service__name b{color:var(--blue)}
.footer{position:absolute;left:0;bottom:0;width:100%;height:41px;background:var(--charcoal)}
.cta{position:absolute;left:50%;transform:translateX(-50%);top:609px;height:20px;padding:0 14px;border-radius:10px;background:var(--blue);color:var(--white);font-size:9.2px;font-weight:700;line-height:20px;white-space:nowrap;z-index:2}
.contact{position:absolute;top:636px;display:flex;align-items:center;gap:4px;color:var(--white);font-size:13px}
.contact--mail{left:36px}
.contact--phone{left:216px}
.contact--web{left:376px}
.device{position:absolute;left:14px;top:314px;width:208px;height:133px;background:linear-gradient(180deg,#2b2d30,#4a4d52 85%,#c8cace);border-radius:6px 6px 2px 2px}
.sds{position:absolute;left:277px;top:310px;width:240px}
.sds__title{font-size:14px;font-weight:700;color:var(--ink);margin-bottom:7px}
.sds__item{margin-bottom:6px}
.sds__label{font-size:11px;font-weight:700;color:var(--blue);line-height:13px}
.sds__text{font-size:10.5px;line-height:12px;color:var(--grey-text)}
</style>
</head>
<body>

<svg width="0" height="0" style="position:absolute">
  <defs>
    <symbol id="tick" viewBox="0 0 14 14">
      <rect x="1" y="2.5" width="10" height="10" rx="1.5" fill="none" stroke="#29a9e1" stroke-width="1.4"/>
      <path d="M3.5 7l2.5 2.5L13 2" fill="none" stroke="#29a9e1" stroke-width="1.6"/>
    </symbol>
    <symbol id="tab-shape" viewBox="0 0 245 28">
      <path d="M0 2h232q4 0 6 4l7 22H0z" fill="#29a9e1"/>
    </symbol>
    <symbol id="ico-mail" viewBox="0 0 14 14">
      <circle cx="7" cy="7" r="6" fill="none" stroke="#fff" stroke-width="1.3"/>
      <circle cx="7" cy="7" r="2.2" fill="none" stroke="#fff" stroke-width="1.2"/>
    </symbol>
    <symbol id="ico-phone" viewBox="0 0 14 14">
      <path d="M3 1.5l2 .2 1 3-1.3 1.2a7 7 0 003.4 3.4L9.3 8l3 1 .2 2-1.6 1.6C6 12.5 1.5 8 1.4 3.1z" fill="none" stroke="#fff" stroke-width="1.2"/>
    </symbol>
    <symbol id="ico-info" viewBox="0 0 14 14">
      <circle cx="7" cy="7" r="6" fill="none" stroke="#fff" stroke-width="1.2"/>
      <path d="M7 6v4.5M7 3.6v1" stroke="#fff" stroke-width="1.4"/>
    </symbol>
  </defs>
</svg>

<!-- Brochure 1: Why we're Kel -->
<section class="brochure brochure--why">
  <header class="masthead">
    <div class="wordmark">KELMORA</div>
    <div class="masthead__tag">KELMORA = RADICAL</div>
  </header>

  <div class="hero" role="img" aria-label="Photo of a smiling man with glasses working on a laptop in a bright office">
    <h1 class="hero__headline">YOUR BUSINESS<br>COMMUNICATIONS<br>DON’T HAVE TO BE LAME!</h1>
  </div>
  <div class="hero-band">
    <div class="hero-band__title">Radically Simple Cloud</div>
    <p class="hero-band__text">Kelmora delivers customized cloud solutions to enterprises and small businesses with the highest level of value, integrity, service, and support radically changing your ability to communicate and compete in the market.</p>
  </div>

  <div class="col col--left">
    <p>100+ years of collective experience activating over 1M user seats, working with some of the largest organizations in the world.</p>
    <p>We leveraged our experiences to build an innovative suite of cloud offerings and features, allowing us to build custom solutions based on unique and changing customer needs.</p>
  </div>
  <div class="col col--right">
    <div class="col__head">Crazy Insane Disaster Proof Network (CIDPN)</div>
    <p>The only way our network is going down if if a meteor shower simultaneously wipes out our 3 geographical redundant data centers. The statistical likelihood of that happening is virtually non-existent.</p>
    <p>Make your business’s communications not lame system phone system not lame with KELTalk: a radically simple way to communicate!</p>
    <p class="col__lead">KELMORA’s radical cloud solutions are setting the new standard for enterprise grade cloud:</p>
  </div>

  <div class="tab"><svg width="245" height="28"><use href="#tab-shape"/></svg><span>What puts the kel in Kelmora - Simplicity:</span></div>
  <ul class="checklist">
    <li><svg width="14" height="14"><use href="#tick"/></svg>No contracts</li>
    <li><svg width="14" height="14"><use href="#tick"/></svg>No upfront costs or hidden fees</li>
    <li><svg width="14" height="14"><use href="#tick"/></svg>Free installation</li>
    <li><svg width="14" height="14"><use href="#tick"/></svg>Free lifetime training &amp; support</li>
  </ul>

  <div class="services">
    <div class="service">
      <div class="service__badge"><svg width="28" height="26" viewBox="0 0 28 26"><path d="M7 14a5 5 0 010-10 7 7 0 0113 1 4.5 4.5 0 011 9z" fill="none" stroke="#29a9e1" stroke-width="1.6"/><path d="M14 14v5M8 19h12M8 19v3M20 19v3" stroke="#29a9e1" stroke-width="1.4" fill="none"/><circle cx="8" cy="23" r="1.6" fill="#29a9e1"/><circle cx="20" cy="23" r="1.6" fill="#29a9e1"/></svg></div>
      <div class="service__name"><b>KEL</b>Talk</div>
    </div>
    <div class="service">
      <div class="service__badge"><svg width="26" height="26" viewBox="0 0 26 26"><circle cx="13" cy="10" r="5.5" fill="#29a9e1"/><path d="M4 25a9 8 0 0118 0z" fill="#29a9e1"/><path d="M6 11a7 7 0 0114 0" fill="none" stroke="#29a9e1" stroke-width="1.6"/></svg></div>
      <div class="service__name"><b>KEL</b>CallCenter</div>
    </div>
    <div class="service">
      <div class="service__badge"><svg width="32" height="24" viewBox="0 0 32 24"><circle cx="8" cy="8" r="3.5" fill="#29a9e1"/><circle cx="24" cy="8" r="3.5" fill="#29a9e1"/><circle cx="16" cy="7" r="4" fill="#29a9e1"/><path d="M2 20a6 6 0 0112 0zM18 20a6 6 0 0112 0z" fill="#29a9e1"/><path d="M9 22a7 7 0 0114 0z" fill="#29a9e1"/></svg></div>
      <div class="service__name"><b>KEL</b>Meetings</div>
    </div>
    <div class="service">
      <div class="service__badge"><svg width="26" height="22" viewBox="0 0 26 22"><rect x="2" y="2" width="22" height="14" rx="1.5" fill="none" stroke="#29a9e1" stroke-width="1.8"/><rect x="5" y="5" width="16" height="8" fill="#29a9e1"/><path d="M9 20h8M13 16v4" stroke="#29a9e1" stroke-width="1.8"/></svg></div>
      <div class="service__name"><b>KEL</b>Apps</div>
    </div>
  </div>

  <div class="cta">Make your business communications not lame, contact KELMORA today!</div>
  <footer class="footer"></footer>
  <div class="contact contact--mail"><svg width="13" height="13"><use href="#ico-mail"/></svg>sales@kelmora.com</div>
  <div class="contact contact--phone"><svg width="13" height="13"><use href="#ico-phone"/></svg>&nbsp;555-014-2290</div>
  <div class="contact contact--web"><svg width="12" height="12"><use href="#ico-info"/></svg>www.kelmora.com</div>
</section>

<!-- Brochure 2: KELTalk -->
<section class="brochure brochure--talk">
  <header class="masthead">
    <div class="wordmark">KELMORA</div>
    <div class="masthead__tag masthead__tag--bold">YOUR PHONE SYSTEM DOESN’T HAVE TO BE LAME.</div>
  </header>

  <div class="hero" role="img" aria-label="Photo of a smiling woman with glasses talking on a desk phone at her laptop"></div>
  <div class="hero-band">KELMORA’s radical hosted VOiP solution KELTalk is setting the new standard for<br>enterprise grade voice</div>

  <div class="device" role="img" aria-label="Laptop showing a KELTalk plan comparison table"></div>

  <div class="sds">
    <div class="sds__title">Super Duper Simple (SDS):</div>
    <div class="sds__item"><div class="sds__label">SET-UP</div><div class="sds__text">Simple user discovery process, custom provisioning to your needs</div></div>
    <div class="sds__item"><div class="sds__label">INSTALLATION</div><div class="sds__text">Virtually plug &amp; play, your custom configuration up and running in minutes</div></div>
    <div class="sds__item"><div class="sds__label">TRAINING</div><div class="sds__text">Simple, intuitive training to allow you to focus on your business. On the web, over the phone, or in person</div></div>
    <div class="sds__item"><div class="sds__label">MANAGEMENT</div><div class="sds__text">Access and manage from any web enabled device, tablet, or P.</div></div>
    <div class="sds__item"><div class="sds__label">SUPPORT</div><div class="sds__text">Support that matches your business needs 24/7/365. We take care of our customers. Plain and simple.</div></div>
    <div class="sds__item"><div class="sds__label">SCALABILITY</div><div class="sds__text">Add users and features to grow with your business</div></div>
  </div>

  <div class="tab"><svg width="245" height="28"><use href="#tab-shape"/></svg><span>What puts the kel in Kelmora - Simplicity:</span></div>
  <ul class="checklist">
    <li><svg width="14" height="14"><use href="#tick"/></svg>No contracts</li>
    <li><svg width="14" height="14"><use href="#tick"/></svg>No upfront costs or hidden fees</li>
    <li><svg width="14" height="14"><use href="#tick"/></svg>Free installation</li>
    <li><svg width="14" height="14"><use href="#tick"/></svg>Free lifetime training &amp; support</li>
  </ul>

  <div class="cta">Make your phone system not lame with KELTalk: a radically simple way to communicate!</div>
  <footer class="footer"></footer>
  <div class="contact contact--mail"><svg width="13" height="13"><use href="#ico-mail"/></svg>sales@kelmora.com</div>
  <div class="contact contact--phone"><svg width="13" height="13"><use href="#ico-phone"/></svg>&nbsp;555-014-2290</div>
  <div class="contact contact--web"><svg width="12" height="12"><use href="#ico-info"/></svg>www.kelmora.com</div>
</section>

</body>
</html>
```